Startup FinTech / Behavioural Science company needs website redesign

We are a startup company interested in redesigning our website. We have most of our content created already (viewable at www.tallyfern.co), but are interested in an upgraded look and feel. We are happy to adjust content as well based on design input. We will move hosting from hostbirch to webmarlo or similar hosting service, so portability of files is important to us. Our team will have the ability to make minor tweaks/content adjustments, but would look to engage with someone for more-comprehensive enhancements in the future.
Updates

Project Deadline Extended
Reason: Other business needs prevented me from providing timely feedback. I will work on feedback over the next two days but wanted to give additional time for design submissions and revisions.

Target Market(s)

Financial advisors in the US and UK, as well as potential end-users of the tools and potential investors

Industry/Entity Type

Information Technology

Coding

Coded - Design and coding required

Number of Pages Required

1 page

Font styles to use
Sans Serif

Requirements
Must have
• - Lighter, cleaner look and feel. We believe our current website is too heavy and "angular."
• - improved iconography to convey behavioural finance concepts (e.g., herd mentality, and illusion of control)
• - links to social media sites
• - integration with our hostbirch personality profile (viewable now at https://deanmollow.formquill.com/to/qRtZbe. Note: we will change this URL to tallyfern.formquill.com... as a part of the design process)
Nice to have
• - ability for us to add a tab/link to a blog in the future.
• - design that allows us to add additional
• - ability for us to add additional pages (e.g., results from our personality profiles, pages to customize sharing on social media)
• - simple ability to enter an email address to add to our mailing list/request more info
• - mobile-responsive design
Should not have
• - Should not have items like office directions and maps, since we are a virtual team.
• - Contact information (e.g., phone number) should be lower down the page vs. at the top
• - comments boxes or lengthy web forms. A simple name/email address is sufficient.

```html
<!DOCTYPE html>
<html lang="en">
<head>
<meta charset="utf-8">
<title>Tallyfern — Behavioural Finance</title>
<link href="https://fonts.googleapis.com/css2?family=Montserrat:wght@400;500;600;700&family=Lato:wght@300;400;700&display=swap" rel="stylesheet">
<style>
:root{
  --purple:#7b2b90;
  --purple-dark:#5e1f70;
  --purple-soft:#a467b4;
  --ink:#2b2b2b;
  --text:#6b6b6b;
  --muted:#9a9a9a;
  --line:#e6e6e6;
  --panel:#f3f3f3;
  --white:#ffffff;
  --footer:#232323;
}
*{box-sizing:border-box;margin:0;padding:0}
html,body{width:1200px;height:4433px;overflow:hidden}
body{position:relative;background:var(--white);font-family:'Lato',sans-serif;color:var(--text)}
section,header,footer{position:absolute;left:0;width:1200px}
.abs{position:absolute}
.center{left:0;width:1200px;text-align:center}
.sec-title{font-family:'Montserrat',sans-serif;font-weight:500;font-size:36px;color:var(--ink)}
.sec-rule{width:30px;height:4px;background:var(--purple);left:585px}

/* header */
.site-header{top:0;height:83px;background:var(--white)}
.brand{left:86px;top:20px;font-family:'Montserrat',sans-serif;font-weight:600;font-size:36px;color:var(--purple);display:flex;align-items:center;gap:10px}
.brand-dot{width:14px;height:14px;border-radius:50%;background:var(--purple)}
.nav{right:90px;top:30px;display:flex;gap:36px;font-family:'Montserrat',sans-serif;font-weight:700;font-size:11px;letter-spacing:.5px;color:var(--ink);text-transform:uppercase}
.nav a{color:inherit;text-decoration:none;padding:8px 0}
.nav a.active{background:var(--purple);color:var(--white);padding:8px 14px;border-radius:3px;margin-top:-1px}

/* hero */
.hero{top:83px;height:562px;background:linear-gradient(135deg,#3a3542 0%,#5a5262 40%,#463e4c 70%,#2f2a33 100%)}
.hero-shade{inset:0;background:linear-gradient(180deg,rgba(60,30,70,.35),rgba(40,20,50,.55))}
.hero-kicker{top:166px;font-family:'Lato',sans-serif;font-weight:300;font-size:28px;color:#e9e4ec}
.hero-title{top:198px;font-family:'Montserrat',sans-serif;font-weight:600;font-size:46px;letter-spacing:2px;color:var(--white)}
.hero-sub{top:256px;font-family:'Montserrat',sans-serif;font-weight:700;font-size:24px;color:var(--white)}
.btn{display:inline-flex;align-items:center;gap:10px;border-radius:22px;font-family:'Montserrat',sans-serif;font-weight:500;font-size:14px;text-decoration:none}
.btn-ring{width:18px;height:18px;border:1.5px solid currentColor;border-radius:50%;display:inline-flex;align-items:center;justify-content:center}
.hero-btn{top:322px;left:536px;padding:10px 22px;background:var(--purple);color:var(--white)}
.hero-chevron{left:588px;top:530px}

/* problem */
.problem{top:645px;height:366px}
.problem .sec-title{top:88px}
.problem .sec-rule{top:136px}
.problem-copy{top:180px;left:340px;width:520px;text-align:center;font-size:15px;line-height:22px;color:var(--text)}
.problem-copy p+p{margin-top:14px}

.why{top:1011px;height:668px;background:var(--panel)}
.why-photo{left:0;top:0;width:340px;height:470px;background:radial-gradient(ellipse at 40% 45%,#f4e7e5 0%,#ece6e4 45%,rgba(243,243,243,0) 75%)}
.why-copy{top:86px;left:330px;width:540px;text-align:center;font-size:14px;line-height:20px}
.why-copy .small{margin-top:28px;font-size:12px;font-weight:700;color:#555}
.why-title{top:286px;font-family:'Montserrat',sans-serif;font-weight:500;font-size:30px;color:var(--ink)}
.concepts{top:348px;left:251px;display:flex;gap:24px}
.concept{width:162px;height:156px;background:var(--purple);border-radius:8px;box-shadow:0 3px 0 var(--purple-dark);display:flex;flex-direction:column;align-items:center;justify-content:center;gap:10px;color:var(--white);font-family:'Montserrat',sans-serif;font-weight:700;font-size:11px;text-align:center;line-height:14px;text-transform:uppercase}
.why-tag{top:572px;font-family:'Montserrat',sans-serif;font-size:22px;color:#555;letter-spacing:.5px}

/* solution */
.solution{top:1679px;height:656px}
.solution .sec-title{top:108px}
.solution .sec-rule{top:174px}
.sol-photo{left:103px;top:236px;width:488px;height:385px;background:linear-gradient(135deg,#e8e3d8 0%,#cfd4dc 45%,#b7c3d3 70%,#5a6f93 100%)}
.quote-box{left:585px;top:242px;width:520px;height:373px;border:16px solid #eeeeee;background:var(--white)}
.quote{left:80px;top:60px;width:330px;font-family:'Lato',sans-serif;font-weight:300;font-size:25px;line-height:40px;color:#444}
.quote-by{left:80px;top:270px;font-family:'Montserrat',sans-serif;font-size:12px;font-weight:600;color:#444;letter-spacing:.5px}

.method{top:2335px;height:385px;background:linear-gradient(180deg,#ffffff 0%,#f4f4f6 60%,#f0eff3 100%)}
.method-shade{right:80px;top:0;width:500px;height:385px;background:radial-gradient(ellipse at 60% 60%,rgba(200,198,206,.45),rgba(240,239,243,0) 70%)}
.method-title{top:96px;font-family:'Montserrat',sans-serif;font-size:22px;color:#555;letter-spacing:.5px}
.steps{left:174px;top:178px;width:900px;display:grid;grid-template-columns:430px 430px;row-gap:36px;column-gap:40px}
.step{display:flex;gap:18px}
.step-icon{flex:none;width:44px;height:44px;border:2px solid var(--purple);border-radius:50%;display:flex;align-items:center;justify-content:center}
.step h3{font-family:'Montserrat',sans-serif;font-weight:700;font-size:14px;color:var(--purple);margin-bottom:4px}
.step p{font-size:14px;line-height:19px;color:#666;width:340px}

/* team */
.team{top:2720px;height:650px}
.team .sec-title{top:100px}
.team .sec-rule{top:174px}
.member{top:221px;width:502px}
.member-photo{width:502px;height:201px}
.member-name{margin-top:38px;font-family:'Lato',sans-serif;font-weight:300;font-size:31px;color:#333}
.member-role{margin-top:10px;font-size:13px;font-weight:700;color:#333}
.member-bio{margin-top:4px;font-size:13px;line-height:17px;color:#777}
.member-link{margin-top:10px;display:flex;align-items:center;gap:8px;font-size:13px;color:var(--purple);text-decoration:none}
.member-link .btn-ring{width:16px;height:16px}

/* take profile */
.cta{top:3370px;height:479px;background:linear-gradient(180deg,#a25aa9 0%,#8b3f96 40%,#a868b0 80%,#c799cd 100%)}
.cta-ghost{top:92px;font-family:'Montserrat',sans-serif;font-weight:700;font-size:38px;color:rgba(255,255,255,.16);letter-spacing:2px}
.cta-title{top:110px;font-family:'Montserrat',sans-serif;font-weight:500;font-size:36px;color:var(--white)}
.cta-sub{top:214px;font-family:'Lato',sans-serif;font-weight:300;font-size:30px;color:var(--white)}
.cta-btn{top:288px;left:521px;padding:10px 22px;background:var(--white);color:var(--purple)}

/* contact */
.contact{top:3849px;height:496px}
.contact .sec-title{top:90px}
.contact-info{left:260px;top:168px;width:322px;text-align:right;font-size:14px;line-height:20px;color:#666}
.contact-info dt{font-family:'Montserrat',sans-serif;font-weight:700;font-size:13px;color:#333}
.contact-info dd{margin-bottom:8px}
.socials{display:flex;justify-content:flex-end;gap:8px;margin-top:4px}
.socials span{width:28px;height:28px;border-radius:50%;background:#3b5c9c}
.socials span:nth-child(2){background:#3fa6df}
.socials span:nth-child(3){background:#1c76b4}
.contact-mark{left:590px;top:235px;width:12px;height:12px;background:var(--purple);transform:rotate(45deg)}
.form{left:615px;top:168px;width:322px}
.field{display:block;width:322px;height:38px;background:#f0f0f0;border:0;margin-bottom:8px;padding:0 12px;font:14px 'Lato',sans-serif;color:#999}
.field.area{height:86px;padding-top:10px}
.send{margin-top:28px;width:148px;height:40px;border-radius:20px;background:var(--purple);color:var(--white);font:600 15px 'Montserrat',sans-serif;display:flex;align-items:center;justify-content:center}

.site-footer{top:4345px;height:88px;background:var(--footer);color:#bbb;font-size:12px}
.footer-copy{left:70px;top:38px}
.footer-top{right:80px;top:36px;display:flex;align-items:center;gap:10px}
</style>
</head>
<body>

<header class="site-header">
  <div class="brand abs"><span class="brand-dot"></span>tallyfern</div>
  <nav class="nav abs">
    <a class="active" href="#problem">The Problem</a>
    <a href="#solution">The Solution</a>
    <a href="#team">Our Team</a>
    <a href="#profile">Take Profile</a>
    <a href="#contact">Contact</a>
  </nav>
</header>

<section class="hero" role="img" aria-label="Photo of people working at a desk with laptops and paperwork">
  <div class="hero-shade abs"></div>
  <div class="hero-kicker abs center">Money Decisions</div>
  <h1 class="hero-title abs center">CAN STRESS YOU OUT</h1>
  <div class="hero-sub abs center">tallyfern can help</div>
  <a class="btn hero-btn abs" href="#problem">Learn More <span class="btn-ring"><svg width="8" height="8" viewBox="0 0 8 8"><path d="M2 1l3 3-3 3" stroke="#fff" stroke-width="1.4" fill="none"/></svg></span></a>
  <svg class="hero-chevron abs" width="24" height="14" viewBox="0 0 24 14"><path d="M2 2l10 10L22 2" stroke="#fff" stroke-width="2.5" fill="none"/></svg>
</section>

<section class="problem" id="problem">
  <h2 class="sec-title abs center">The Problem</h2>
  <div class="sec-rule abs"></div>
  <div class="problem-copy abs">
    <p>Money and financial issues are the leading causes of anxiety for most of us. This financial stress is among the leading causes of divorce, addiction, obesity and depression.</p>
    <p>What’s worse, the consequences of the decisions that we make can make us even more stressed, not more relieved.</p>
  </div>
</section>

<section class="why">
  <div class="why-photo abs" role="img" aria-label="Soft photo of a piggy bank and coins"></div>
  <div class="why-copy abs">
    <p>Ask anyone the key to good physical health, and you’re likely to get a correct answer: don’t overeat, choose healthy foods and exercise regularly. The path to good physical health is not a mystery, but we have a hard time following it.</p>
    <p class="small">Good financial health works the same way. We generally know what to do – spend less than we earn, save for a rainy day, and make non-emotional investment decisions – but have a hard time doing it.</p>
  </div>
  <h2 class="why-title abs center">WHY?</h2>
  <div class="concepts abs">
    <div class="concept">
      <svg width="54" height="54" viewBox="0 0 54 54" fill="none" stroke="#fff" stroke-width="2"><path d="M19 30a12 12 0 1 1 16 0c-2 2-3 4-3 7H22c0-3-1-5-3-7z"/><path d="M22 42h10M23 46h8"/><path d="M27 14v-6M13 20l-4-4M41 20l4-4"/></svg>
      <span>Short-term<br>thinking</span>
    </div>
    <div class="concept">
      <svg width="64" height="54" viewBox="0 0 64 54" fill="none" stroke="#fff" stroke-width="2"><circle cx="32" cy="14" r="6"/><path d="M22 44V30a10 10 0 0 1 20 0v14"/><circle cx="14" cy="20" r="5"/><path d="M6 46V34a8 8 0 0 1 14-5"/><circle cx="50" cy="20" r="5"/><path d="M58 46V34a8 8 0 0 0-14-5"/></svg>
      <span>Herd<br>mentality</span>
    </div>
    <div class="concept">
      <svg width="54" height="54" viewBox="0 0 54 54" fill="none" stroke="#fff" stroke-width="2"><rect x="10" y="16" width="26" height="26" rx="4" transform="rotate(-15 23 29)"/><circle cx="18" cy="24" r="1.8" fill="#fff"/><circle cx="26" cy="32" r="1.8" fill="#fff"/><path d="M36 12l8 8M42 8l4 4M30 8l2 2"/></svg>
      <span>Gambler’s<br>fallacy</span>
    </div>
    <div class="concept">
      <svg width="60" height="54" viewBox="0 0 60 54" fill="none" stroke="#fff" stroke-width="2"><path d="M14 16h32a8 8 0 0 1 8 8l2 14a5 5 0 0 1-9 3l-5-7H18l-5 7a5 5 0 0 1-9-3l2-14a8 8 0 0 1 8-8z"/><path d="M18 22v8M14 26h8"/><circle cx="40" cy="23" r="1.8" fill="#fff"/><circle cx="45" cy="28" r="1.8" fill="#fff"/><path d="M30 16V8"/></svg>
      <span>Illusion of<br>control</span>
    </div>
  </div>
  <div class="why-tag abs center">THIS IS WHERE TALLYFERN COMES IN.</div>
</section>

<section class="solution" id="solution">
  <h2 class="sec-title abs center">The Solution</h2>
  <div class="sec-rule abs"></div>
  <div class="sol-photo abs" role="img" aria-label="Photo of a hand filling in a financial form with a pen"></div>
  <div class="quote-box abs">
    <p class="quote abs">“Once you have ordinary intel-ligence, what you need is the temperament to control the urges that get other people in to trouble in investing.”</p>
    <div class="quote-by abs">- HARLAN VOSS</div>
  </div>
</section>

<section class="method">
  <div class="method-shade abs" role="img" aria-label="Faint photo of people in silhouette"></div>
  <h2 class="method-title abs center">THE TALLYFERN SOLUTION</h2>
  <div class="steps abs">
    <div class="step">
      <span class="step-icon"><svg width="22" height="22" viewBox="0 0 22 22" fill="none" stroke="#7b2b90" stroke-width="1.8"><circle cx="11" cy="7" r="4"/><path d="M3 20a8 8 0 0 1 16 0"/></svg></span>
      <div><h3>Take the profile</h3><p>Take the Tallyfern profile to learn more about your financial personality and tendencies</p></div>
    </div>
    <div class="step">
      <span class="step-icon"><svg width="22" height="22" viewBox="0 0 22 22" fill="none" stroke="#7b2b90" stroke-width="1.8"><path d="M8 14l6-6"/><path d="M10 6l2-2a4 4 0 0 1 6 6l-2 2M12 16l-2 2a4 4 0 0 1-6-6l2-2"/></svg></span>
      <div><h3>Connect your accounts</h3><p>Connect your financial accounts to see your opportunities to be a better saver and investor</p></div>
    </div>
    <div class="step">
      <span class="step-icon"><svg width="22" height="22" viewBox="0 0 22 22" fill="none" stroke="#7b2b90" stroke-width="1.8"><rect x="3" y="9" width="16" height="11"/><path d="M3 13h16M11 9v11M11 9c-2-5-7-4-5-1M11 9c2-5 7-4 5-1"/></svg></span>
      <div><h3>Gain better insight</h3><p>Play the investment simulation to gain better insight into your strengths and weaknesses</p></div>
    </div>
    <div class="step">
      <span class="step-icon"><svg width="22" height="22" viewBox="0 0 22 22" fill="none" stroke="#7b2b90" stroke-width="1.8"><path d="M3 3v16h16"/><path d="M6 15l4-5 3 3 5-6"/></svg></span>
      <div><h3>Check your progress</h3><p>Check your progress over time to stay on track</p></div>
    </div>
  </div>
</section>

<section class="team" id="team">
  <h2 class="sec-title abs center">Our Team</h2>
  <div class="sec-rule abs"></div>
  <article class="member abs" style="left:83px">
    <div class="member-photo" role="img" aria-label="Portrait photo of Dean Mollow" style="background:linear-gradient(90deg,#6b6e66 0%,#8b8a80 45%,#4b4a45 100%)"></div>
    <h3 class="member-name">Dean Mollow, CFA</h3>
    <div class="member-role">CEO / Head of “Fin”</div>
    <div class="member-bio">FinTech Veteran &nbsp;|&nbsp; Investment Portfolio Manager<br>Thamesgate Business School &nbsp;|&nbsp; Kestrel Ridge University</div>
    <a class="member-link" href="#">Profile <span class="btn-ring"><svg width="7" height="7" viewBox="0 0 8 8"><path d="M2 1l3 3-3 3" stroke="#7b2b90" stroke-width="1.4" fill="none"/></svg></span></a>
  </article>
  <article class="member abs" style="left:612px">
    <div class="member-photo" role="img" aria-label="Portrait photo of Owen Halbrook" style="background:linear-gradient(90deg,#9a9b9e 0%,#6e6f73 50%,#b4b5b8 100%)"></div>
    <h3 class="member-name">Owen Halbrook</h3>
    <div class="member-role">CTO / Head of “Tech”</div>
    <div class="member-bio">Data Science Expert &nbsp;|&nbsp; Predictive Analytics Solution Architect<br>Alder Vale University &nbsp;|&nbsp; Baymont University</div>
    <a class="member-link" href="#">Profile <span class="btn-ring"><svg width="7" height="7" viewBox="0 0 8 8"><path d="M2 1l3 3-3 3" stroke="#7b2b90" stroke-width="1.4" fill="none"/></svg></span></a>
  </article>
</section>

<section class="cta" id="profile">
  <div class="cta-ghost abs center">TAKE PROFILE</div>
  <h2 class="cta-title abs center">Take Profile</h2>
  <p class="cta-sub abs center">Want to learn about your financial personality?</p>
  <a class="btn cta-btn abs" href="https://tallyfern.formquill.com">Learn Now <span class="btn-ring"><svg width="8" height="8" viewBox="0 0 8 8"><path d="M2 1l3 3-3 3" stroke="#7b2b90" stroke-width="1.4" fill="none"/></svg></span></a>
</section>

<section class="contact" id="contact">
  <h2 class="sec-title abs center">Contact</h2>
  <dl class="contact-info abs">
    <dt>Phone:</dt>
    <dd>+1 555 014 7781 &nbsp;|&nbsp; +44 7700 900 318</dd>
    <dt>Email:</dt>
    <dd>info@tallyfern.co</dd>
    <dt>Social Media</dt>
    <dd><div class="socials"><span></span><span></span><span></span></div></dd>
  </dl>
  <div class="contact-mark abs"></div>
  <div class="form abs">
    <div class="field" style="line-height:38px">Name</div>
    <div class="field" style="line-height:38px">Email Address</div>
    <div class="field area">Your Message</div>
    <div class="send">Send</div>
  </div>
</section>

<footer class="site-footer">
  <div class="footer-copy abs">© Tallyfern | All Rights Reserved</div>
  <div class="footer-top abs">Back to top <svg width="14" height="8" viewBox="0 0 14 8"><path d="M1 7l6-6 6 6" stroke="#bbb" stroke-width="1.6" fill="none"/></svg></div>
</footer>

</body>
</html>
```